Small Firewood bag design (for use it retail stores NZ)

Hi, we are a small business in New Zealand selling firewood. We have started to bag our wood and are now selling to stores in NZ. We are in need of a good firewood bag design. The overall size to be 40cm high x 25cm wide, however the text should be at minimum 2cm within this, as to prevent it from going around the corner of the bag.
We will only be printing the label on 1 side of the bag, and would like a design for black printing only and a design with black and orange/flame color.
Our business is called 'Kettle Ridge Firewood', (KRF Limited)
The product/wood type is Black Wattle.
The wood is a very hardwood, makes a great burner, burns hot and long, especially when compared to pine.
Our firewood is naturally seasoned outside in the northland sun.
Black wattle is of the Acacia family from Australia.
The bags are only small, 12kg or 25 litres.
It will be printed onto clear woven PP bags, see image. So intricate drawings is not recommended.
There will be no barcode on the label, as this will be sewn onto the bag separately.
Can provide our contact details for the bag later.

Note, the below images I designed on an online AI program, but do quite like the look of them.

Target Market(s)

Will be for sale in large department stores, petrol stations, some liquor stores and some dairy's. Target market is older people, people going to the batch, wood for people not organized to get in bulk amounts of wood

Industry/Entity Type

Firewood, home heating, winter, cold

Colors

Designer to choose colors to be used in the design.

Requirements
Nice to have
• Possibly an image of logs with the flames around it

```html
<!DOCTYPE html>
<html lang="en">
<head>
<meta charset="utf-8">
<title>Kettle Ridge Firewood – Black Wattle 12kg Bag</title>
<link rel="stylesheet" href="https://fonts.googleapis.com/css2?family=Germania+One&display=swap">
<style>
  :root {
    --bag-black: #060607;
    --frame-orange: #e0541f;
    --brand-amber: #ef8d17;
    --brand-amber-light: #f6b13a;
    --species-peach: #eaa484;
    --species-orange: #d9582a;
    --species-edge: #f2a07c;
    --tagline-amber: #f29a16;
    --weight-amber: #f5a00f;
    --badge-navy: #2b3a8f;
    --badge-white: #f7f7f7;
    --badge-red: #d6232f;
  }
  * { margin: 0; padding: 0; box-sizing: border-box; }
  html, body {
    width: 750px;
    height: 1200px;
    overflow: hidden;
    background: var(--bag-black);
  }
  .bag-label {
    position: relative;
    width: 750px;
    height: 1200px;
    background: var(--bag-black);
    font-family: "Germania One", "Georgia", serif;
    overflow: hidden;
  }
  .frame-lines {
    position: absolute;
    inset: 0;
    pointer-events: none;
  }
  .corner-ornament {
    position: absolute;
    width: 164px;
    height: 164px;
  }
  .corner-ornament--tl { left: 14px; top: 10px;
    background: radial-gradient(circle at 0 0, rgba(224,84,31,0.45), rgba(224,84,31,0) 70%); }
  .corner-ornament--tr { right: 14px; top: 10px;
    background: radial-gradient(circle at 100% 0, rgba(224,84,31,0.45), rgba(224,84,31,0) 70%); }
  .corner-ornament--bl { left: 14px; bottom: 10px;
    background: radial-gradient(circle at 0 100%, rgba(224,84,31,0.45), rgba(224,84,31,0) 70%); }
  .corner-ornament--br { right: 14px; bottom: 10px;
    background: radial-gradient(circle at 100% 100%, rgba(224,84,31,0.45), rgba(224,84,31,0) 70%); }

  .brand-name {
    position: absolute;
    top: 100px;
    left: 0;
    width: 100%;
    text-align: center;
    font-size: 60px;
    line-height: 1;
    letter-spacing: 1px;
    text-transform: uppercase;
    background: linear-gradient(180deg, var(--brand-amber-light), var(--brand-amber) 70%);
    -webkit-background-clip: text;
    background-clip: text;
    color: transparent;
  }
  .species-name {
    position: absolute;
    top: 250px;
    left: 0;
    width: 100%;
    text-align: center;
    text-transform: uppercase;
    font-size: 118px;
    line-height: 138px;
    letter-spacing: 2px;
    background: linear-gradient(180deg, var(--species-peach) 0%, var(--species-orange) 45%, var(--species-orange) 100%);
    -webkit-background-clip: text;
    background-clip: text;
    color: transparent;
    -webkit-text-stroke: 1.5px var(--species-edge);
  }
  .species-name span { display: block; }
  .tagline {
    position: absolute;
    top: 558px;
    left: 0;
    width: 100%;
    text-align: center;
    color: var(--tagline-amber);
    font-size: 21px;
    line-height: 36px;
    text-transform: uppercase;
    letter-spacing: 0.3px;
  }
  .fire-illustration {
    position: absolute;
    left: 76px;
    top: 630px;
    width: 610px;
    height: 515px;
    background:
      radial-gradient(ellipse 34% 38% at 50% 62%, rgba(255,200,60,0.9), rgba(240,110,20,0.75) 45%, rgba(150,40,15,0.35) 75%, rgba(0,0,0,0) 100%),
      radial-gradient(ellipse 50% 30% at 50% 85%, rgba(110,40,25,0.8), rgba(40,15,10,0.4) 70%, rgba(0,0,0,0) 100%);
  }
  .origin-badge {
    position: absolute;
    left: 82px;
    top: 1022px;
    width: 96px;
    height: 96px;
  }
  .pack-weight {
    position: absolute;
    right: 77px;
    top: 1080px;
    color: var(--weight-amber);
    font-size: 50px;
    line-height: 1;
  }
</style>
</head>
<body>
  <main class="bag-label">
    <svg class="frame-lines" width="750" height="1200" viewBox="0 0 750 1200" aria-hidden="true">
      <g stroke="var(--frame-orange)" stroke-width="2" fill="none">
        <line x1="15" y1="10" x2="256" y2="10"/>
        <line x1="493" y1="10" x2="737" y2="10"/>
        <line x1="14" y1="10" x2="14" y2="244"/>
        <line x1="736" y1="10" x2="736" y2="244"/>
        <line x1="15" y1="1189" x2="256" y2="1189"/>
        <line x1="493" y1="1189" x2="737" y2="1189"/>
        <line x1="14" y1="958" x2="14" y2="1189"/>
        <line x1="736" y1="958" x2="736" y2="1189"/>
      </g>
    </svg>
    <div class="corner-ornament corner-ornament--tl" role="img" aria-label="Scrolled orange corner flourish"></div>
    <div class="corner-ornament corner-ornament--tr" role="img" aria-label="Scrolled orange corner flourish"></div>
    <div class="corner-ornament corner-ornament--bl" role="img" aria-label="Scrolled orange corner flourish"></div>
    <div class="corner-ornament corner-ornament--br" role="img" aria-label="Scrolled orange corner flourish"></div>

    <h1 class="brand-name">Kettle Ridge Firewood</h1>

    <h2 class="species-name"><span>Black</span><span>Wattle</span></h2>

    <p class="tagline">
      A very hardwood, makes a great burner, burns hot and long<br>
      Naturally seasoned outside in the Northland sun
    </p>

    <div class="fire-illustration" role="img" aria-label="Illustration of stacked logs burning in a roaring fire with sparks and split wood pieces"></div>

    <svg class="origin-badge" viewBox="0 0 96 96" aria-hidden="true">
      <circle cx="48" cy="48" r="47" fill="var(--badge-white)"/>
      <circle cx="48" cy="48" r="43" fill="var(--badge-navy)"/>
      <circle cx="48" cy="48" r="28" fill="var(--badge-white)" stroke="var(--badge-red)" stroke-width="3"/>
    </svg>

    <div class="pack-weight">12KG</div>
  </main>
</body>
</html>
```